Sales presentation for Veltro-7

Veltro-7.com is a digital intelligence service which provides news and analysis about digital business models and ecosystems. The readers are C-Suite executives such as chief executive officers, chief marketing officers, chief information officers, strategists, company directors and internet entrepreneurs.

.

Target Market(s)

The audience for the presentation are strategy managers and media buyers at advertising agencies and marketing managers of technology companies and professional service companies.

Industry/Entity Type

Sales

Requirements
Must have
• Slides 9 and 10 have rough diagrams that need to be professionally designed.
Nice to have
• Slide 12 could do with a better piece of generic art

```html
<!DOCTYPE html>
<html lang="en">
<head>
<meta charset="utf-8">
<title>Veltro-7 Sales Presentation – Slide Redesign</title>
<link rel="stylesheet" href="https://fonts.googleapis.com/css2?family=Open+Sans:wght@400;600;700&family=Arimo:wght@400;700&family=Kaushan+Script&display=swap">
<style>
  :root {
    --frame-blue: #7ea8d3;
    --frame-edge: #5d8cbf;
    --slide-white: #ffffff;
    --title-blue: #4a7ebb;
    --quote-blue: #1f73c2;
    --ink: #1a1a1a;
    --body-grey: #404040;
    --wordmark-grey: #3a3a3a;
    --segment-blue: #7ea8d3;
    --banner-black: #111111;
    --arrow-red: #e02020;
    --page-bg: #ffffff;
  }
  * { margin: 0; padding: 0; box-sizing: border-box; }
  html, body { width: 1200px; height: 1000px; overflow: hidden; background: var(--page-bg); }
  .canvas { position: relative; width: 1200px; height: 1000px; overflow: hidden; font-family: "Arimo", Arial, sans-serif; color: var(--ink); }

  .slide {
    position: absolute;
    background: var(--slide-white);
    border: 14px solid var(--frame-blue);
    outline: 2px solid var(--frame-edge);
    outline-offset: -16px;
    box-shadow: 3px 4px 8px rgba(0,0,0,.35);
    overflow: hidden;
  }
  .slide-title { left: 0; top: -10px; width: 595px; height: 455px; z-index: 1; }
  .slide-aldane { left: 597px; top: 50px; width: 603px; height: 456px; z-index: 2; }
  .slide-traditional { left: 0; top: 445px; width: 595px; height: 440px; z-index: 3; }

  /* Title slide */
  .brand { position: absolute; left: 0; right: 0; top: 58px; display: flex; justify-content: center; align-items: center; gap: 10px; }
  .brand-mark { width: 18px; height: 18px; background: var(--wordmark-grey); }
  .brand-name { font-family: "Open Sans", Arial, sans-serif; font-weight: 600; font-size: 36px; line-height: 44px; color: var(--wordmark-grey); }
  .presenter-name { position: absolute; left: 0; right: 0; top: 178px; text-align: center; font-family: "Open Sans", Arial, sans-serif; font-weight: 700; font-size: 31px; color: var(--title-blue); padding-left: 20px; }
  .presenter-role { position: absolute; left: 0; right: 0; top: 222px; text-align: center; font-size: 15px; padding-left: 20px; }
  .quote { position: absolute; font-size: 16px; line-height: 21px; }
  .quote .quote-text { color: var(--quote-blue); }
  .quote-first { left: 32px; top: 288px; }
  .quote-second { left: 227px; top: 349px; }

  .slide-heading { position: absolute; left: 0; right: 0; text-align: center; font-family: "Open Sans", Arial, sans-serif; font-weight: 600; color: var(--title-blue); text-decoration: underline; text-underline-offset: 4px; }

  /* Aldane slide */
  .slide-aldane .slide-heading { top: 26px; font-size: 31px; }
  .point-list { position: absolute; left: 34px; top: 131px; width: 236px; list-style: none; font-family: "Open Sans", Arial, sans-serif; font-size: 12px; line-height: 16.5px; color: var(--body-grey); }
  .point-list li { position: relative; padding-left: 24px; margin-bottom: 4px; }
  .point-list li::before { content: "✻"; position: absolute; left: 0; top: 0; color: #9a9a9a; font-size: 11px; }
  .model-wheel { position: absolute; left: -611px; top: -64px; width: 1200px; height: 1000px; }
  .wheel-caption { position: absolute; left: 300px; width: 270px; top: 372px; text-align: center; font-size: 16px; line-height: 20px; color: var(--title-blue); }

  /* Traditional slide */
  .slide-traditional .slide-heading { top: 22px; font-size: 30px; }
  .trad-point { position: absolute; left: 24px; top: 96px; font-family: "Open Sans", Arial, sans-serif; font-size: 20px; line-height: 31.5px; color: var(--ink); padding-left: 22px; }
  .trad-point::before { content: "✻"; position: absolute; left: 0; top: 0; color: #9a9a9a; font-size: 18px; }
  .control-diagram { position: absolute; left: -14px; top: -459px; width: 1200px; height: 1000px; }

  /* Photo placeholders */
  .portrait { position: absolute; box-shadow: 2px 3px 6px rgba(0,0,0,.4); }
  .portrait-reflection { position: absolute; opacity: .35; -webkit-mask-image: linear-gradient(to bottom, rgba(0,0,0,.8), transparent); mask-image: linear-gradient(to bottom, rgba(0,0,0,.8), transparent); }
  .tone-panel { background: linear-gradient(160deg, #c9d6e4, #7d8a99); }
  .tone-grey { background: linear-gradient(160deg, #d8d4cf, #8a7f79); }
  .tone-warm { background: linear-gradient(160deg, #b79b7c, #4d3a2c); }
  .tone-field { background: linear-gradient(160deg, #a7a78c, #7b6f5e); }
  .tone-light { background: linear-gradient(160deg, #ece8ee, #8c7f8f); }
  .tone-studio { background: linear-gradient(160deg, #f2efec, #c7b6a3); }

  /* Annotations */
  .annotation-arrows { position: absolute; left: 0; top: 0; width: 1200px; height: 1000px; z-index: 10; pointer-events: none; }
  .annotation { position: absolute; z-index: 11; font-family: "Kaushan Script", cursive; font-size: 34px; line-height: 48px; color: #ffffff; text-align: center;
    text-shadow: -2px -2px 0 #000, 2px -2px 0 #000, -2px 2px 0 #000, 2px 2px 0 #000, 0 -2px 0 #000, 0 2px 0 #000, -2px 0 0 #000, 2px 0 0 #000, 3px 4px 4px rgba(0,0,0,.5); }
  .note-backgrounds { left: 480px; top: 68px; width: 230px; }
  .note-diagrams-right { left: 815px; top: 276px; width: 280px; }
  .note-reflection { left: 592px; top: 716px; width: 270px; }
  .note-diagrams-left { left: 62px; top: 856px; width: 280px; }
</style>
</head>
<body>
<main class="canvas">

  <section class="slide slide-title" aria-label="Title slide">
    <div class="brand"><span class="brand-mark"></span><span class="brand-name">Veltro-7</span></div>
    <h1 class="presenter-name">Daniel Harrow</h1>
    <p class="presenter-role">Editor and Publisher. September 2013</p>
    <p class="quote quote-first"><span class="quote-text">“There has been a huge increase in the number of<br>CEOs taking control of digital strategy”</span> Brightwell &amp;<br>Partners, 2013</p>
    <p class="quote quote-second"><span class="quote-text">“By 2016 the CMO will spend more on IT<br>than the IT manager”</span><br>Corvane Research, 2012</p>
  </section>

  <section class="slide slide-aldane" aria-label="Aldane model slide">
    <h2 class="slide-heading">Aldane model</h2>
    <ul class="point-list">
      <li>The Aldane model turns the traditional model around on itself putting the customer at the centre of the conversation.</li>
      <li>The model recognises that customers want to apply their own interests to content</li>
      <li>By editorialising your content marketing we amplify your story to our readers in a way that engages their interest, matches their workflow and promote share-ability</li>
    </ul>
    <svg class="model-wheel" viewBox="0 0 1200 1000" aria-label="Content wheel diagram">
      <g fill="var(--segment-blue)" stroke="#ffffff" stroke-width="3">
        <path d="M946.6 233.6 A125 125 0 0 1 1035 197 L1035 260 A62 62 0 0 0 991.2 278.2 Z"/>
        <path d="M1035 197 A125 125 0 0 1 1123.4 233.6 L1078.8 278.2 A62 62 0 0 0 1035 260 Z"/>
        <path d="M1123.4 233.6 A125 125 0 0 1 1160 322 L1097 322 A62 62 0 0 0 1078.8 278.2 Z"/>
        <path d="M1160 322 A125 125 0 0 1 1123.4 410.4 L1078.8 365.8 A62 62 0 0 0 1097 322 Z"/>
        <path d="M1123.4 410.4 A125 125 0 0 1 1035 447 L1035 384 A62 62 0 0 0 1078.8 365.8 Z"/>
        <path d="M1035 447 A125 125 0 0 1 946.6 410.4 L991.2 365.8 A62 62 0 0 0 1035 384 Z"/>
        <path d="M946.6 410.4 A125 125 0 0 1 910 322 L973 322 A62 62 0 0 0 991.2 365.8 Z"/>
        <path d="M910 322 A125 125 0 0 1 946.6 233.6 L991.2 278.2 A62 62 0 0 0 973 322 Z"/>
      </g>
      <g fill="#ffffff" font-family="Open Sans, Arial, sans-serif" font-weight="700" text-anchor="middle" letter-spacing="0.3">
        <text x="999" y="239" font-size="9">Advertising</text>
        <text x="1071" y="240" font-size="11">News</text>
        <text x="1121" y="290" font-size="11">Features</text>
        <text x="1121" y="362" font-size="11">Opinion</text>
        <text x="1071" y="405" font-size="11">Guest<tspan x="1071" dy="13">Columns</tspan></text>
        <text x="999" y="405" font-size="11">Special<tspan x="999" dy="13">Reports</tspan></text>
        <text x="949" y="355" font-size="9">Custom<tspan x="949" dy="11">Publishing</tspan></text>
        <text x="949" y="289" font-size="9">Advertorial</text>
      </g>
    </svg>
    <p class="wheel-caption">In the Aldane model customers<br>determine the value of content</p>
  </section>

  <section class="slide slide-traditional" aria-label="Traditional model slide">
    <h2 class="slide-heading">Traditional model</h2>
    <p class="trad-point">Traditional publishing models track a linear<br>path of publisher/advertiser engagement<br>from full editorial control to full client control.<br>But customers are excluded from this<br>conversation</p>
    <svg class="control-diagram" viewBox="0 0 1200 1000" aria-label="Publisher to advertiser control diagram">
      <g font-family="Open Sans, Arial, sans-serif" font-weight="700" font-size="11" fill="#111">
        <text x="44" y="745">Publisher</text>
        <text x="289" y="747" text-anchor="middle">Control</text>
        <text x="543" y="745" text-anchor="end">Advertiser</text>
      </g>
      <g stroke="#111" stroke-width="3" fill="#111">
        <line x1="126" y1="742" x2="233" y2="742"/>
        <polygon points="117,742 130,735 130,749" stroke="none"/>
        <line x1="344" y1="742" x2="448" y2="742"/>
        <polygon points="458,742 445,735 445,749" stroke="none"/>
      </g>
      <g fill="var(--segment-blue)" stroke="#ffffff" stroke-width="2">
        <rect x="28" y="753" width="56" height="71"/>
        <rect x="84" y="753" width="66" height="71"/>
        <rect x="150" y="753" width="66" height="71"/>
        <rect x="216" y="753" width="66" height="71"/>
        <rect x="282" y="753" width="66" height="71"/>
        <rect x="348" y="753" width="72" height="71"/>
        <rect x="420" y="753" width="73" height="71"/>
        <rect x="493" y="753" width="71" height="71"/>
      </g>
      <g fill="#ffffff" font-family="Open Sans, Arial, sans-serif" font-weight="700" font-size="9.5" text-anchor="middle" letter-spacing="0.3">
        <text x="50" y="794">News</text>
        <text x="117" y="794">Features</text>
        <text x="183" y="794">Opinion</text>
        <text x="249" y="789">Guest<tspan x="249" dy="11">Columns</tspan></text>
        <text x="315" y="789">Special<tspan x="315" dy="11">Reports</tspan></text>
        <text x="384" y="789">Custom<tspan x="384" dy="11">Publishing</tspan></text>
        <text x="456" y="794">Advertorial</text>
        <text x="529" y="794">Advertising</text>
      </g>
      <rect x="33" y="824" width="527" height="14" fill="var(--banner-black)"/>
      <text x="296" y="835" fill="#ffffff" font-family="Open Sans, Arial, sans-serif" font-weight="700" font-size="9.5" text-anchor="middle" letter-spacing="0.5">The old model assumes quality decayed during the journey from editorial to advertising</text>
    </svg>
  </section>

  <div class="portrait tone-panel" role="img" aria-label="Photo of a speaker seated at a conference panel desk" style="left:640px;top:517px;width:123px;height:150px;"></div>
  <div class="portrait-reflection tone-panel" style="left:640px;top:669px;width:123px;height:40px;"></div>
  <div class="portrait tone-grey" role="img" aria-label="Photo of a presenter gesturing at a microphone" style="left:808px;top:517px;width:167px;height:158px;"></div>
  <div class="portrait-reflection tone-grey" style="left:808px;top:677px;width:167px;height:40px;"></div>
  <div class="portrait tone-warm" role="img" aria-label="Portrait photo of a thoughtful businessman" style="left:1008px;top:517px;width:152px;height:150px;"></div>
  <div class="portrait-reflection tone-warm" style="left:1008px;top:669px;width:152px;height:40px;"></div>
  <div class="portrait tone-field" role="img" aria-label="Close-up portrait photo of a smiling man with glasses" style="left:632px;top:735px;width:158px;height:167px;"></div>
  <div class="portrait-reflection tone-field" style="left:632px;top:904px;width:158px;height:60px;"></div>
  <div class="portrait tone-light" role="img" aria-label="Portrait photo of a young woman in a patterned top" style="left:808px;top:738px;width:167px;height:179px;"></div>
  <div class="portrait-reflection tone-light" style="left:808px;top:919px;width:167px;height:60px;"></div>
  <div class="portrait tone-studio" role="img" aria-label="Studio portrait photo of a smiling businesswoman" style="left:1001px;top:737px;width:159px;height:213px;"></div>
  <div class="portrait-reflection tone-studio" style="left:1001px;top:952px;width:159px;height:48px;"></div>

  <svg class="annotation-arrows" viewBox="0 0 1200 1000" aria-hidden="true">
    <g stroke="var(--arrow-red)" stroke-width="4" fill="var(--arrow-red)" stroke-linecap="round">
      <line x1="437" y1="84" x2="576" y2="35"/>
      <polygon points="590,30 572,26 578,44" stroke="none"/>
      <line x1="808" y1="297" x2="945" y2="241"/>
      <polygon points="960,236 942,232 949,250" stroke="none"/>
      <line x1="575" y1="735" x2="712" y2="687"/>
      <polygon points="727,682 709,678 715,696" stroke="none"/>
      <line x1="50" y1="870" x2="188" y2="822"/>
      <polygon points="203,817 185,813 191,831" stroke="none"/>
    </g>
  </svg>
  <div class="annotation note-backgrounds">New Cool<br>Backgrounds</div>
  <div class="annotation note-diagrams-right">New professional<br>diagrams</div>
  <div class="annotation note-reflection">Reflection Pictures</div>
  <div class="annotation note-diagrams-left">New professional<br>diagrams</div>

</main>
</body>
</html>
```